Web Design Project

The aim of this project to design a website for a service that would offer services for small business and non profit organizations using opensource software that is weaved to work together in harmony.

The website name is: velisto.net

Tavrel in Arabic means: cabbage. Cabbage is composed of leaves, actually there is nothing except leaves. Each leave by itself is not called cabbage, but a collection of leaves that are organized in a central way would give us cabbage.

Same idea for Tavrel where open source software very well organized and integrated would create a new thing with a new value.
Updates

Target Market(s)

Small business, Europe, Africa, Far east and Middle east

Industry/Entity Type

Small Business

Requirements
Must have
• The website would offer the following sections:
* Home page
* Benefits: value of tavrel
* Applications: applications offered by tavrel
* Pricing
* Purchase
* Customer log in
* Support
- FAQ
- Knowledge base
- Forums
- Open tickets

Please take the following consideration in design:
* White should predominate
* Only black and the colors of logo are permitted (attched)
Nice to have
• Design is better to express:
* Openness
* Dynamic
* Usable
* Cost effective

```html
<!DOCTYPE html>
<html lang="en">
<head>
<meta charset="utf-8">
<title>tavrel</title>
<link href="https://fonts.googleapis.com/css2?family=Didact+Gothic&display=swap" rel="stylesheet">
<style>
:root{
  --ink:#222;
  --text:#555;
  --muted:#777;
  --rule:#9a9a9a;
  --green:#8dc63f;
  --pink:#b2489b;
  --blue:#2b8fc8;
  --nav-active:#8a8a8a;
  --white:#fff;
}
*{box-sizing:border-box;margin:0;padding:0}
html,body{width:1123px;height:1200px;overflow:hidden;background:var(--white)}
body{position:relative;font-family:"Didact Gothic",sans-serif;color:var(--text)}
a{color:inherit;text-decoration:none}
.abs{position:absolute}

.brand{left:55px;top:40px;display:flex;align-items:center;gap:10px}
.brand-dot{width:22px;height:22px;border-radius:50%;background:var(--pink)}
.brand-name{font-size:44px;color:var(--ink);letter-spacing:-0.5px;line-height:1}

.top-links{left:462px;top:102px;font-size:16px;color:var(--text)}
.top-links span{margin:0 6px;color:var(--muted)}
.welcome{left:868px;top:96px;display:flex;align-items:center;gap:10px;font-size:16px;color:var(--text)}
.welcome b{font-weight:normal;color:var(--green)}

.main-nav{left:55px;top:157px;width:1027px;height:29px;border-top:1px solid var(--rule);border-bottom:1px solid var(--rule);display:flex;align-items:center}
.main-nav a{font-size:16px;padding:0 12.5px;height:27px;line-height:27px;color:var(--text)}
.main-nav a.active{background:var(--nav-active);color:var(--white);padding:0 7px}
.search{margin-left:auto;display:flex;align-items:center;gap:36px;padding-right:6px}
.search span{font-size:14px;font-style:italic;color:#999}

.hero-main{left:56px;top:217px;width:679px;height:359px;background:radial-gradient(circle at 45% 40%,#f0d2ae 0%,#d79a55 35%,#9a5a26 70%,#6d3c18 100%)}
.hero-side{left:750px;top:217px;width:332px;height:361px;background:linear-gradient(180deg,#e9edef 0%,#cfd6da 40%,#8c5a3f 55%,#6a8fb2 100%)}
.panel{color:var(--white);text-align:center;font-size:16px;line-height:23.6px}
.panel-pink{background:rgba(178,72,155,.78)}
.panel-blue{background:rgba(43,143,200,.85)}
.quote{left:484px;top:248px;width:223px;height:161px;padding-top:12px}
.band{left:56px;top:504px;width:679px;height:72px;padding-top:11px;background:rgba(178,72,155,.62)}
.side-band{left:750px;top:451px;width:332px;height:127px;padding-top:15px}

.section-title{left:56px;top:614px;font-size:23px;color:var(--text);letter-spacing:.3px}
.product{top:652px;width:241px}
.product-media{height:162px;border:1px solid #ddd;position:relative}
.product p{margin-top:14px;font-size:16px;line-height:23.6px;color:var(--text)}
.media-green{background:linear-gradient(135deg,#9fd27a,#7dba55)}
.media-green .cart{position:absolute;left:76px;top:28px;text-align:center;color:var(--white);font-size:16px}
.media-clinic{background:linear-gradient(90deg,#e8ece9 0%,#d9e4e3 40%,#c3ccd4 100%)}
.media-cloud{background:linear-gradient(180deg,#f6f7f8,#e6eaee)}
.media-tech{background:radial-gradient(circle at 55% 45%,#6ab3de 0%,#2b4c6a 45%,#141b24 100%)}

.footer-col{top:991px;font-size:13.5px;line-height:19px}
.footer-col h3{font-weight:normal;font-size:16px;color:var(--text);margin-bottom:10px}
.footer-col li{list-style:none}
.newsletter{left:843px;top:983px;width:210px;font-size:13.5px;line-height:17px}
.email{margin-top:11px;width:208px;height:27px;border:1px solid #ccc;display:flex;align-items:center;justify-content:space-between;padding:0 4px 0 4px;font-size:14px;color:#888}
.email i{width:18px;height:18px;border:1px solid #bbb;border-radius:2px;background:#f2f2f2;display:flex;align-items:center;justify-content:center}
.copyright{left:56px;top:1166px;font-size:13.5px}
</style>
</head>
<body>

<header>
  <div class="abs brand"><span class="brand-dot"></span><span class="brand-name">tavrel</span></div>
  <nav class="abs top-links"><a href="#">Log In</a><span>|</span><a href="#">Register</a><span>|</span><a href="#">Support</a><span>|</span><a href="#">FAQ</a></nav>
  <div class="abs welcome">
    <svg width="26" height="32" viewBox="0 0 26 32" aria-hidden="true"><circle cx="13" cy="5" r="4.5" fill="#777"/><path d="M2 12h22v20h-5V17h-2v15h-8V17H7v15H2z" fill="#777"/></svg>
    <span>WELCOME <b>YOURNAME</b></span>
  </div>
  <nav class="abs main-nav">
    <a class="active" href="#">home</a><a href="#">benefits</a><a href="#">applications</a><a href="#">pricing</a><a href="#">purchase</a><a href="#">knowledge base</a><a href="#">forums</a><a href="#">open tickets</a>
    <div class="search"><span>search for something here</span>
      <svg width="20" height="20" viewBox="0 0 20 20" aria-hidden="true"><circle cx="8" cy="8" r="6" fill="none" stroke="#666" stroke-width="2.4"/><path d="M12.5 12.5l5.5 5.5" stroke="#666" stroke-width="2.8" stroke-linecap="round"/></svg>
    </div>
  </nav>
</header>

<section>
  <div class="abs hero-main" role="img" aria-label="Photo of a smiling woman outdoors in warm autumn light"></div>
  <div class="abs panel panel-pink quote">Lorem ipsum dolor sit<br>amet, consectetur<br>adipiscing elit.<br>Nunc elit erat, tincidunt<br>quis tempus vel,<br>iaculis quis ligula.</div>
  <div class="abs panel band">Lorem ipsum dolor sit amet, consectetur adipiscing elit.<br>Nunc elit erat, tincidunt quis tempus vel, iaculis quis ligula.</div>
  <div class="abs hero-side" role="img" aria-label="Photo of a family on a leather sofa with a laptop"></div>
  <div class="abs panel panel-blue side-band">Lorem ipsum dolor sit amet, consectetur<br>adipiscing elit.<br>Nunc elit erat, tincidunt<br>quis tempus vel, iaculis quis ligula.</div>
</section>

<section>
  <h2 class="abs section-title" style="font-weight:normal">NEW PRODUCTS</h2>
  <article class="abs product" style="left:55px">
    <div class="product-media media-green" role="img" aria-label="Photo of electronic devices and circuit boards">
      <div class="cart">
        <svg width="70" height="56" viewBox="0 0 70 56" aria-hidden="true"><path d="M2 6h10l8 30h38l8-22H16" fill="none" stroke="#fff" stroke-width="4" stroke-linejoin="round"/><circle cx="26" cy="48" r="5" fill="#fff"/><circle cx="52" cy="48" r="5" fill="#fff"/></svg>
        <div style="margin-top:6px">Add to cart</div>
      </div>
    </div>
    <p>Lorem ipsum dolor sit amet, con-sectetur adipiscing elit. Nunc elit erat, tincidunt quis tempus vel, iaculis quis ligula.</p>
  </article>
  <article class="abs product" style="left:317px">
    <div class="product-media media-clinic" role="img" aria-label="Photo of medical staff in a hospital room with equipment"></div>
    <p>Lorem ipsum dolor sit amet, con-sectetur adipiscing elit. Nunc elit erat, tincidunt quis tempus vel, iaculis quis ligula.</p>
  </article>
  <article class="abs product" style="left:580px">
    <div class="product-media media-cloud" role="img" aria-label="Illustration of a blue cloud behind a laptop"></div>
    <p>Lorem ipsum dolor sit amet, con-sectetur adipiscing elit. Nunc elit erat, tincidunt quis tempus vel, iaculis quis ligula.</p>
  </article>
  <article class="abs product" style="left:842px">
    <div class="product-media media-tech" role="img" aria-label="Photo of a hand touching glowing digital icons in a server room"></div>
    <p>Lorem ipsum dolor sit amet, con-sectetur adipiscing elit. Nunc elit erat, tincidunt quis tempus vel, iaculis quis ligula.</p>
  </article>
</section>

<footer>
  <div class="abs footer-col" style="left:56px"><h3>INFORMATION</h3><ul><li>Terms and Conditions</li><li>Privacy Policy</li><li>About Us</li></ul></div>
  <div class="abs footer-col" style="left:318px"><h3>YOUR ACCOUNT</h3><ul><li>Log In</li><li>Register</li><li>Newsletter Subscriptions</li></ul></div>
  <div class="abs footer-col" style="left:579px"><h3>CONTACTS</h3>
    <p style="line-height:24px">Lorem ipsum dolor sit amet,<br>consectetur adipiscing elit.</p>
    <p style="margin-top:14px">Telephone: +00 00000<br>000000<br>E-mail: mail@yoursite.com</p>
  </div>
  <div class="abs newsletter">
    <p>Subscribe to our free monthly newsletter and be the first to hear about our offers.</p>
    <div class="email"><span>Email..</span><i><svg width="8" height="10" viewBox="0 0 8 10" aria-hidden="true"><path d="M2 1l4 4-4 4" fill="none" stroke="#888" stroke-width="1.6"/></svg></i></div>
  </div>
  <div class="abs copyright">© 2013 All Rights Reserved</div>
</footer>

</body>
</html>
```